Local soccer team website - Canberra Iron Kestrels FC

Wanting a redesign of our existing website (https://www.canberraikfc-demo.com.au) in an editable WIX template transferred to our account. Color scheme is Red, Blue and White and we will supply the logo which we already have. We want the same style of website with the same headings/pages, with most of the data on the one page with anchors etc. To reiterate we want this template editable in WIX and transferred to us as part of the price.

Target Market(s)

fans and players

Industry/Entity Type

sports

Coding

Coded - Design and coding required

Number of Pages Required

3 page

Font styles to use
Sans Serif

Requirements
Must have
• Pages: Home, About, The Team, Contact, Juniors, Womens
Nice to have
• home, about, the team and contact to all be on the one page with anchor links. juniors and womens to have their own page. wix template transferred to our account. red, blue and white theme (similar to logo), black also ok.

```html
<!DOCTYPE html>
<html lang="en">
<head>
<meta charset="utf-8">
<title>Canberra Iron Kestrels FC</title>
<link href="https://fonts.googleapis.com/css2?family=Montserrat:wght@500;600;700;800&family=Lato:wght@400;700&display=swap" rel="stylesheet">
<style>
:root{
  --red:#f20d0d;
  --blue:#1b5be3;
  --blue-deep:#0f46c8;
  --ink:#111111;
  --text:#333333;
  --paper:#ffffff;
  --mist:#f4f4f4;
  --line:#dcdcdc;
  --map-base:#eceeea;
  --map-green:#c9e2c0;
  --map-park:#b7d9aa;
}
*{margin:0;padding:0;box-sizing:border-box}
html,body{width:1200px;height:3309px;overflow:hidden}
body{position:relative;background:var(--paper);font-family:"Lato",sans-serif;color:var(--text)}
.abs{position:absolute}

/* hero */
.hero{left:0;top:0;width:1200px;height:699px;background:linear-gradient(100deg,#2c2d2a 0%,#3b3c36 35%,#5a4a42 60%,#3a3d45 100%)}
.hero-photo{left:0;top:0;width:1200px;height:699px;background:radial-gradient(ellipse at 72% 45%,rgba(160,60,60,.55),rgba(40,40,40,0) 55%),linear-gradient(180deg,rgba(0,0,0,.15),rgba(0,0,0,.35))}
.brand{left:120px;top:34px;width:150px;color:#fff;font-family:"Montserrat",sans-serif;font-weight:700;font-size:15px;line-height:20px;letter-spacing:.3px}
.top-cta{left:952px;top:10px;width:135px;height:38px;background:var(--red);color:#fff;font-family:"Montserrat",sans-serif;font-weight:700;font-size:14px;display:flex;align-items:center;justify-content:center}
.nav{top:76px;color:#fff;font-size:15px}
.hero-title{left:113px;top:232px;color:#fff;font-family:"Montserrat",sans-serif;font-weight:800;font-size:50px;line-height:61px;letter-spacing:.5px}
.hero-sub{left:114px;top:430px;color:#fff;font-family:"Montserrat",sans-serif;font-weight:700;font-size:18px}
.hero-btn{left:113px;top:486px;width:160px;height:46px;border:2px solid #fff;color:#fff;font-family:"Montserrat",sans-serif;font-weight:700;font-size:15px;display:flex;align-items:center;justify-content:center}

/* team */
.section-title{font-family:"Montserrat",sans-serif;font-weight:700;color:var(--ink)}
.team-title{left:0;top:760px;width:1200px;text-align:center;font-size:36px}
.team-card{top:863px;width:465px;height:449px;border:1px solid var(--line);background:#fff}
.team-photo{width:100%;height:333px}
.team-card h3{font-family:"Montserrat",sans-serif;font-weight:700;font-size:28px;color:var(--ink);text-align:center;margin-top:42px}

/* about */
.about{left:0;top:1394px;width:1200px;height:740px;background:linear-gradient(90deg,#1f4fbf 0%,#1b55d6 45%,var(--blue) 100%)}
.about-tag{left:44px;top:1474px;color:rgba(255,255,255,.35);font-family:"Montserrat",sans-serif;font-weight:800;font-size:15px}
.about-title{left:109px;top:1458px;color:#fff;font-family:"Montserrat",sans-serif;font-weight:700;font-size:36px}
.about-sub{left:109px;top:1527px;color:#fff;font-family:"Montserrat",sans-serif;font-weight:500;font-size:21px;line-height:30px}
.about-rule{left:636px;top:1561px;width:182px;height:1px;background:rgba(255,255,255,.8)}
.about-body{left:636px;top:1586px;width:460px;color:#fff;font-size:15px;line-height:25.7px}
.about-body p{margin-bottom:25px}
.about-body .honours{font-weight:700;margin-bottom:10px}
.about-body .list{margin:0}
.about-btn{left:640px;top:1998px;width:178px;height:58px;border:2px solid #fff;color:#fff;font-family:"Montserrat",sans-serif;font-weight:700;font-size:17px;display:flex;align-items:center;justify-content:center}

/* map */
.map{left:0;top:2134px;width:1200px;height:518px;
  background:
    radial-gradient(ellipse 260px 200px at 880px 330px,var(--map-park) 0%,rgba(183,217,170,0) 100%),
    radial-gradient(ellipse 220px 170px at 280px 180px,var(--map-park) 0%,rgba(183,217,170,0) 100%),
    radial-gradient(ellipse 300px 180px at 760px 90px,var(--map-green) 0%,rgba(201,226,192,0) 100%),
    radial-gradient(ellipse 260px 200px at 1100px 430px,var(--map-green) 0%,rgba(201,226,192,0) 100%),
    radial-gradient(ellipse 240px 160px at 90px 420px,var(--map-green) 0%,rgba(201,226,192,0) 100%),
    linear-gradient(180deg,#f1f2ef 0%,var(--map-base) 100%)}

/* contact */
.contact{left:0;top:2652px;width:1200px;height:560px;background:var(--mist)}
.contact-divider{left:600px;top:2652px;width:1px;height:560px;background:var(--line)}
.contact-title{left:96px;top:2722px;font-size:41px}
.register{left:100px;top:2805px;font-family:"Montserrat",sans-serif;font-weight:700;font-size:17px;color:var(--ink)}
.email-field{left:102px;top:2850px;width:450px;height:49px;border:1px solid #555;background:#fff;font-size:15px;color:#333;padding-left:28px;display:flex;align-items:center}
.submit{left:102px;top:2918px;width:450px;height:48px;background:var(--red);color:#fff;font-family:"Montserrat",sans-serif;font-weight:700;font-size:13px;display:flex;align-items:center;justify-content:center}
.info h4{position:absolute;font-family:"Montserrat",sans-serif;font-weight:700;font-size:25px;color:var(--ink)}
.info p{position:absolute;font-size:15px;line-height:23px;color:var(--text)}

/* footer */
.footer{left:0;top:3212px;width:1200px;height:97px;background:#fff;display:flex;align-items:center;justify-content:center;font-size:14.5px;color:var(--text);word-spacing:2px}
</style>
</head>
<body>

<header>
  <div class="abs hero"></div>
  <div class="abs hero-photo" role="img" aria-label="Club captain in red and blue kit running on the pitch with a ball, spectators behind"></div>
  <div class="abs brand">Canberra Iron Kestrels FC</div>
  <a class="abs top-cta">CONTACT US</a>
  <nav>
    <span class="abs nav" style="left:591px">Home</span>
    <span class="abs nav" style="left:669px">About</span>
    <span class="abs nav" style="left:748px">The Team</span>
    <span class="abs nav" style="left:852px">Contact</span>
    <span class="abs nav" style="left:942px">Juniors</span>
    <span class="abs nav" style="left:1029px">Womens</span>
  </nav>
  <h1 class="abs hero-title">WELCOME TO<br>THE CANBERRA IRON<br>KESTRELS FC WEBSITE</h1>
  <div class="abs hero-sub">CANBERRA IKFC</div>
  <a class="abs hero-btn">CONTACT US</a>
</header>

<section>
  <h2 class="abs section-title team-title">THE TEAM</h2>
  <article class="abs team-card" style="left:116px">
    <div class="team-photo" role="img" aria-label="NPL2 squad team photo on a grass field" style="background:linear-gradient(180deg,#8aa6c4 0%,#a9b7b8 35%,#6d7f47 60%,#5e7a3a 100%)"></div>
    <h3>The 2023 NPL2 Team</h3>
  </article>
  <article class="abs team-card" style="left:621px">
    <div class="team-photo" role="img" aria-label="Reserves team celebrating with a champions banner" style="background:linear-gradient(180deg,#6f7a6c 0%,#8a5a5e 40%,#7a3a44 65%,#3d4f7a 100%)"></div>
    <h3>The 2023 reserves Team</h3>
  </article>
</section>

<section>
  <div class="abs about" role="img" aria-label="Club marquee and supporters at a match day, tinted blue"></div>
  <div class="abs about-tag">THIS IS</div>
  <h2 class="abs about-title">ABOUT</h2>
  <div class="abs about-sub">About our Club<br>Canberra Iron Kestrels FC</div>
  <div class="abs about-rule"></div>
  <div class="abs about-body">
    <p>The Canberra Iron Kestrels FC (or commonly known simply as Iron Kestrels) is an Australian amateur association football club based in the ACT. The club was founded in 1992 by the Canberra Tuggeranong community and currently competes in the ACT NPL2 competition.</p>
    <p>The club has a successful history in winning both the minor premiership and finals in what used to be State League 1, Capital League and also spent 2 years in the Canberra Premier League.</p>
    <p class="honours">ACT Capital League Premiers and Finals Champions.</p>
    <p class="list">Premiers (7): 1994, 2004, 2009, 2010, 2011, 2012, 2013, 2019<br>Runner-up (2): 2014, 2016<br>Champions (7): 2003, 2004, 2007, 2008, 2009, 2011, 2012<br>Runner-up (2): 2010, 2015</p>
  </div>
  <a class="abs about-btn">Learn More</a>
</section>

<div class="abs map" role="img" aria-label="Street map of the Woden Valley area with parks and suburbs, marking the club ground location"></div>

<section>
  <div class="abs contact"></div>
  <div class="abs contact-divider"></div>
  <h2 class="abs section-title contact-title">CONTACT US</h2>
  <div class="abs register">REGISTER FOR NEWS</div>
  <div class="abs email-field">Email Address</div>
  <div class="abs submit">SUBMIT</div>
  <div class="info">
    <h4 style="left:705px;top:2731px">Our Address:</h4>
    <p style="left:705px;top:2780px">Corner of Harlow and Fenwick Streets<br>Phillip, ACT 2606</p>
    <h4 style="left:705px;top:2887px">Getting Here</h4>
    <p style="left:706px;top:2933px">There is limited parking within the grounds,<br>additional parking is available across the street</p>
    <h4 style="left:705px;top:3023px">Email</h4>
    <p style="left:706px;top:3070px">info@canberraikfc-demo.com.au</p>
  </div>
</section>

<footer class="abs footer">©Copyrights 2023 &nbsp;Canberra Iron Kestrels &nbsp;| &nbsp;&nbsp;All Rights Reserved</footer>

</body>
</html>
```